Northern Horizons Published Photographer Website

I need a website to feature a home page slide show of 6 of my top photos then a few simple pages including; gallery, bio, social, checkout, services

Target Market(s)

photography

Industry/Entity Type

Photographer

Coding

Coded - Design and coding required

Number of Pages Required

5+ page

Colors

Designer to choose colors to be used in the design.

Requirements
Must have
• clean eye catching elegant trendy
Nice to have
• unique and creative from other photographer websites

```html
<!DOCTYPE html>
<html lang="en">
<head>
<meta charset="utf-8">
<title>Elise Marlowe Photography</title>
<link href="https://fonts.googleapis.com/css2?family=Libre+Baskerville&family=Oswald:wght@300;400;500&family=Lato:wght@300;400;700&display=swap" rel="stylesheet">
<style>
:root{
  --black:#000;
  --ink:#0d0d0d;
  --panel:#111;
  --white:#fff;
  --paper:#f2f2f2;
  --grey:#8a8a8a;
  --line:#3a3a3a;
  --gold:#c9a46a;
  --text-dark:#333;
  --field:#2b2b2b;
}
*{margin:0;padding:0;box-sizing:border-box}
html,body{width:1200px;height:5088px;overflow:hidden;background:var(--black)}
body{position:relative;font-family:"Lato",sans-serif;color:var(--white)}
.abs{position:absolute}

/* header + hero */
.hero{left:0;top:0;width:1200px;height:595px;
  background:linear-gradient(180deg,#6f7a76 0%,#4f5a3a 35%,#3c4a24 60%,#2a2a1a 100%)}
.hero-photo{position:absolute;inset:0;
  background:radial-gradient(ellipse at 50% 55%,#d9dcd6 0 8%,transparent 22%),
  linear-gradient(90deg,#2e3b1a 0%,#5a6a30 25%,#b9b8a4 50%,#6b5a30 72%,#3a2e18 100%);opacity:.85}
.hero-shade{position:absolute;inset:0;background:linear-gradient(180deg,rgba(0,0,0,.55) 0,rgba(0,0,0,.1) 25%,rgba(0,0,0,.25) 100%)}
.brand{left:170px;top:22px;font-family:"Libre Baskerville",serif;font-size:22px;color:var(--white);display:flex;align-items:center;gap:10px}
.brand .dot{width:16px;height:16px;border-radius:50%;background:var(--white)}
.nav{left:540px;top:44px;display:flex;gap:26px;font-family:"Oswald",sans-serif;font-size:13px;letter-spacing:1px}
.socials-top{left:960px;top:46px;display:flex;gap:10px}
.socials-top span{width:10px;height:10px;border-radius:50%;background:var(--white)}
.hero-title{left:0;top:280px;width:1200px;text-align:center;font-family:"Libre Baskerville",serif;font-size:48px;line-height:64px;color:var(--white)}

/* intro */
.intro{left:0;top:595px;width:1200px;height:465px;background:var(--panel)}
.intro-heading{left:170px;top:670px;font-family:"Oswald",sans-serif;font-size:21px;letter-spacing:.5px}
.intro-text{left:170px;top:712px;width:262px;font-size:13px;line-height:20px;color:var(--grey)}
.btn{display:inline-block;border:1px solid var(--white);font-family:"Oswald",sans-serif;font-size:11px;letter-spacing:1px;padding:6px 14px;color:var(--white)}
.intro-btn{left:170px;top:778px}
.tile{width:272px;height:157px;display:flex;align-items:center;justify-content:center;
  font-family:"Oswald",sans-serif;font-size:30px;letter-spacing:1px;text-shadow:0 2px 6px rgba(0,0,0,.6)}
.t-land{left:458px;top:645px;background:linear-gradient(160deg,#5b7fa6,#8a9b5a 60%,#3e4a22)}
.t-sunset{left:755px;top:645px;background:linear-gradient(180deg,#c46a1a,#f2b43a 50%,#3a1e08)}
.t-sunrise{left:162px;top:845px;background:linear-gradient(180deg,#2a5aa0,#e08a3a 55%,#3a2410)}
.t-wild{left:458px;top:845px;background:linear-gradient(180deg,#9bb6d2,#a08a6a 60%,#6b5a40)}
.t-nature{left:755px;top:845px;background:linear-gradient(160deg,#d7a23a,#7a5a22 50%,#2a2410)}

/* bio */
.bio{left:162px;top:1094px;width:873px;height:314px;background:var(--paper)}
.bio-photo{left:162px;top:1094px;width:360px;height:314px;background:linear-gradient(135deg,#bfc6cf,#e6e0d6 50%,#9aa4ad)}
.bio-label{left:585px;top:1132px;font-size:11px;color:var(--grey)}
.bio-name{left:585px;top:1152px;font-family:"Oswald",sans-serif;font-size:22px;color:var(--text-dark);letter-spacing:.5px}
.bio-text{left:585px;top:1192px;width:400px;font-size:12px;line-height:19px;color:#666}
.bio-btn{left:585px;top:1316px;border-color:var(--text-dark);color:var(--text-dark)}

/* gallery */
.gallery-heading{left:162px;top:1470px;font-family:"Oswald",sans-serif;font-size:22px}
.photo{position:absolute}
.card{position:absolute;background:var(--white);color:var(--text-dark);padding:40px 36px}
.card h3{font-family:"Oswald",sans-serif;font-weight:400;font-size:24px;margin-bottom:16px}
.card p{font-size:12px;line-height:19px;color:#777}
.card .tag{position:absolute;left:50%;bottom:0;width:32px;height:32px;margin-left:-16px;background:var(--ink);display:flex;align-items:center;justify-content:center}
.card.center{text-align:center}

.p1{left:162px;top:1569px;width:538px;height:491px;background:linear-gradient(180deg,#3a7fd0 0%,#9bc2e8 35%,#e4a058 55%,#8a3a1a 75%,#3a1e12 100%)}
.c1{left:636px;top:1781px;width:403px;height:305px}
.p2{left:581px;top:2022px;width:377px;height:492px;background:linear-gradient(180deg,#f4c040 0%,#e08a18 40%,#6a3a08 75%,#1e1206 100%)}
.c2{left:242px;top:2158px;width:403px;height:259px}
.p3{left:162px;top:2514px;width:538px;height:623px;background:linear-gradient(180deg,#2a78d8 0%,#8ab8e8 30%,#d87838 55%,#a84a1e 80%,#5a3018 100%)}
.c3{left:636px;top:2697px;width:403px;height:377px}
.p4{left:581px;top:3108px;width:377px;height:615px;background:linear-gradient(180deg,#3a4a8a 0%,#a07aa8 35%,#e8a070 55%,#6a8aa8 75%,#3a3a3a 100%)}
.c4{left:242px;top:3231px;width:403px;height:407px}
.p5{left:162px;top:3680px;width:538px;height:623px;background:linear-gradient(180deg,#2a4a8a 0%,#7a9ac8 40%,#c8d4e0 55%,#5a5a5a 78%,#2a2a2a 100%)}
.c5{left:636px;top:3862px;width:403px;height:272px}

.more-btn{left:548px;top:4370px}

.rule{left:162px;width:873px;height:1px;background:var(--line)}
.insta-title{left:162px;top:4540px;font-family:"Oswald",sans-serif;font-size:19px}
.insta-sub{left:162px;top:4568px;font-size:11px;color:var(--grey)}
.thumbs{left:330px;top:4503px;display:flex;gap:17px}
.thumbs div{width:93px;height:93px}
.pager{left:988px;top:4604px;display:flex;gap:4px}
.pager span{width:20px;height:20px;background:#555;display:flex;align-items:center;justify-content:center}

/* contact */
.contact-title{left:162px;top:4700px;font-family:"Oswald",sans-serif;font-size:17px}
.field{position:absolute;left:162px;width:275px;height:34px;background:var(--field);font-size:11px;color:#999;padding:10px 12px}
.submit{left:162px;top:4945px;width:275px;height:26px;background:var(--white);color:var(--text-dark);font-family:"Oswald",sans-serif;font-size:11px;letter-spacing:1px;display:flex;align-items:center;justify-content:center}
.news-title{left:466px;top:4726px;font-size:12px;color:#ccc}
.news-field{left:466px;top:4770px;width:438px;height:34px;background:var(--field);font-size:11px;color:#999;padding:10px 12px}
.news-btn{left:904px;top:4770px;width:131px;height:34px;background:var(--gold);color:var(--white);font-family:"Oswald",sans-serif;font-size:12px;letter-spacing:1px;display:flex;align-items:center;justify-content:center}
.socials{left:938px;top:4864px;display:flex;gap:14px}
.socials span{width:12px;height:12px;border-radius:50%;background:var(--white)}

.footer{left:0;top:5024px;width:1200px;height:64px;background:var(--ink);border-top:1px solid var(--line);display:flex;align-items:center;justify-content:center;font-size:12px;color:#ccc}
</style>
</head>
<body>

<header>
  <div class="abs hero">
    <div class="hero-photo" role="img" aria-label="Waterfall in a wooded gorge beneath a tall railway bridge"></div>
    <div class="hero-shade"></div>
  </div>
  <div class="abs brand"><span>Elise Marlowe Photography</span><span class="dot"></span></div>
  <nav class="abs nav"><span>HOME</span><span>ABOUT</span><span>SERVICES</span><span>GALLERY</span><span>CONTACT</span></nav>
  <div class="abs socials-top"><span></span><span></span><span></span><span></span></div>
  <h1 class="abs hero-title">A Good Photograph is Knowing<br>Where to Stand</h1>
</header>

<section>
  <div class="abs intro"></div>
  <h2 class="abs intro-heading">I'M SEARCHING BEAUTY</h2>
  <p class="abs intro-text">Every frame is a quiet search for light, for place, and for the moment the landscape opens up.</p>
  <span class="abs btn intro-btn">VIEW GALLERY</span>
  <div class="abs tile t-land" role="img" aria-label="Landscape photograph">LANDSCAPE</div>
  <div class="abs tile t-sunset" role="img" aria-label="Sunset over water">SUNSETS</div>
  <div class="abs tile t-sunrise" role="img" aria-label="Sunrise through a rock arch">SUNRISES</div>
  <div class="abs tile t-wild" role="img" aria-label="Wild horse in a field">WILDLIFE</div>
  <div class="abs tile t-nature" role="img" aria-label="Golden forest path">NATURE</div>
</section>

<section>
  <div class="abs bio"></div>
  <div class="abs bio-photo" role="img" aria-label="Portrait of the photographer"></div>
  <p class="abs bio-label">Published Photographer</p>
  <h2 class="abs bio-name">ELISE MARLOWE</h2>
  <p class="abs bio-text">My work has been featured by Northern Horizons and travels from quiet lakes to desert canyons, chasing the light that makes each place feel alive.</p>
  <span class="abs btn bio-btn">CONTACT ME</span>
</section>

<section>
  <h2 class="abs gallery-heading">MY GALLERY</h2>

  <div class="photo p1" role="img" aria-label="Sunrise glowing beneath Mesa Arch over a canyon"></div>
  <article class="card c1"><h3>Mesa Arch</h3><p>The sun rises under the arch and spills gold across the canyon below, a morning worth the long cold hike in the dark.</p><span class="tag"><svg width="10" height="10" viewBox="0 0 10 10"><path d="M3 1l4 4-4 4" stroke="#fff" fill="none" stroke-width="1.5"/></svg></span></article>

  <div class="photo p2" role="img" aria-label="Heron silhouetted at a golden sunset by a pier"></div>
  <article class="card c2 center"><h3>Navarre, Florida</h3><p>"Heaven is waiting for the bird"</p><span class="tag"><svg width="10" height="10" viewBox="0 0 10 10"><path d="M3 1l4 4-4 4" stroke="#fff" fill="none" stroke-width="1.5"/></svg></span></article>

  <div class="photo p3" role="img" aria-label="Chapel built into red rock under a blue sky"></div>
  <article class="card c3"><h3>Chapel of the Holy Cross</h3><p>Chapel of the Holy Cross rises from the red rock, a quiet place built right into the stone and the sky.</p><span class="tag"><svg width="10" height="10" viewBox="0 0 10 10"><path d="M3 1l4 4-4 4" stroke="#fff" fill="none" stroke-width="1.5"/></svg></span></article>

  <div class="photo p4" role="img" aria-label="Frosted pine tree against a pastel evening sky"></div>
  <article class="card c4"><h3>Cottonwood, Arizona</h3><p>A single frosted pine stands against the evening sky, the desert cold and still after the first snow of the year. Thank you to all who came out.</p><span class="tag"><svg width="10" height="10" viewBox="0 0 10 10"><path d="M3 1l4 4-4 4" stroke="#fff" fill="none" stroke-width="1.5"/></svg></span></article>

  <div class="photo p5" role="img" aria-label="Glass sphere on a rocky shore reflecting a lake"></div>
  <article class="card c5"><h3>Grundy Lake Provincial Park</h3><p>Life is all about perspective: you never know what a small glass sphere will show at the lake.</p><span class="tag"><svg width="10" height="10" viewBox="0 0 10 10"><path d="M3 1l4 4-4 4" stroke="#fff" fill="none" stroke-width="1.5"/></svg></span></article>

  <span class="abs btn more-btn">VIEW MORE</span>
</section>

<section>
  <div class="abs rule" style="top:4460px"></div>
  <h2 class="abs insta-title">INSTAGRAM FEED</h2>
  <p class="abs insta-sub">@elisemarlowe photography</p>
  <div class="abs thumbs">
    <div role="img" aria-label="Harbour at dusk" style="background:linear-gradient(180deg,#3a5a8a,#c87a3a)"></div>
    <div role="img" aria-label="Lighthouse on rocks" style="background:linear-gradient(180deg,#7a9ac8,#8a5a3a)"></div>
    <div role="img" aria-label="Desert butte" style="background:linear-gradient(180deg,#5a8ad0,#b8602a)"></div>
    <div role="img" aria-label="Red sunset sky" style="background:linear-gradient(180deg,#d84a2a,#3a1a10)"></div>
    <div role="img" aria-label="Orange sunset over lake" style="background:linear-gradient(180deg,#f0a030,#5a2a10)"></div>
    <div role="img" aria-label="Forest clearing" style="background:linear-gradient(180deg,#a8c8d8,#3a5a2a)"></div>
  </div>
  <div class="abs pager">
    <span><svg width="8" height="8" viewBox="0 0 8 8"><path d="M5 1L2 4l3 3" stroke="#fff" fill="none"/></svg></span>
    <span><svg width="8" height="8" viewBox="0 0 8 8"><path d="M3 1l3 3-3 3" stroke="#fff" fill="none"/></svg></span>
  </div>
  <div class="abs rule" style="top:4664px"></div>
</section>

<section>
  <h2 class="abs contact-title">QUICK CONTACT</h2>
  <div class="field" style="top:4738px">Name</div>
  <div class="field" style="top:4782px">Email</div>
  <div class="field" style="top:4826px;height:100px">Message</div>
  <div class="abs submit">SUBMIT</div>
  <p class="abs news-title">Subscribe to our newsletter for latest updates</p>
  <div class="abs news-field">Email</div>
  <div class="abs news-btn">SUBSCRIBE</div>
  <div class="abs socials"><span></span><span></span><span></span><span></span></div>
</section>

<footer class="abs footer">© Copyright Information here</footer>

</body>
</html>
```